Calloway Holdings Website Design

We are a private equity firm based with offices based in Hong Kong, Singapore, London and Paris. Our focus is investments in property development projects, corporate ventures and loans.

We require the development of a new website and you will have to select relevant images from the likes of PixBarrel or other stock photo libraries.

We will need a design done for a PC based website and the designer selected with the favored design will also need to produce some concepts for a responsive website.

Target Market(s)

Sophisticated investors looking to invest in high return property development, businesses and mortgages.

Industry/Entity Type

Investment

Number of Pages Required

5+ page

Font styles to use
Serif
Sans Serif

Colors
0255a3
00a990

Requirements
Must have
• Clean modern feel and must portray stability and professionalism.

```html
<!DOCTYPE html>
<html lang="en">
<head>
<meta charset="utf-8">
<title>Calloway Holdings</title>
<link rel="stylesheet" href="https://fonts.googleapis.com/css2?family=Montserrat:wght@400;500;600;700&family=Open+Sans:wght@400;600&display=swap">
<style>
:root{
  --teal:#00a990;
  --teal-dark:#009a83;
  --navy:#1d2d5c;
  --ink:#3c3c3c;
  --muted:#6f6f6f;
  --line:#dcdcdc;
  --white:#ffffff;
  --hero-top:#5b5650;
  --hero-bottom:#2c2a28;
}
*{margin:0;padding:0;box-sizing:border-box}
html,body{width:761px;height:1200px;overflow:hidden;background:var(--white)}
body{position:relative;font-family:"Open Sans",Arial,sans-serif;color:var(--ink)}
.abs{position:absolute}
.heading{font-family:"Montserrat",Arial,sans-serif}

/* header */
.site-header{left:0;top:0;width:761px;height:38px;background:var(--white)}
.brand{left:172px;top:11px;font-family:"Montserrat",Arial,sans-serif;font-weight:700;font-size:13px;color:var(--navy);letter-spacing:.3px;display:flex;align-items:center;gap:6px}
.brand-mark{width:10px;height:14px;background:var(--navy)}
.nav{top:15px;font-family:"Montserrat",Arial,sans-serif;font-size:5.8px;color:#555;letter-spacing:.3px}
.nav.active{color:var(--teal)}

/* hero */
.hero{left:0;top:38px;width:761px;height:247px;background:linear-gradient(180deg,var(--hero-top),var(--hero-bottom))}
.hero-title{left:0;top:138px;width:761px;text-align:center;font-family:"Montserrat",Arial,sans-serif;font-size:12.5px;color:var(--white);letter-spacing:.4px}
.hero-title b{font-weight:700}
.hero-sub{left:220px;top:158px;width:321px;text-align:center;font-family:"Montserrat",Arial,sans-serif;font-size:5.2px;line-height:9px;color:var(--white);letter-spacing:.2px}
.btn-teal{left:346px;top:196px;width:69px;height:18px;background:var(--teal);color:var(--white);font-family:"Montserrat",Arial,sans-serif;font-weight:600;font-size:6px;letter-spacing:.5px;display:flex;align-items:center;justify-content:center}
.dot{width:5px;height:5px;border-radius:50%;border:1px solid var(--white)}
.dot.on{background:var(--teal);border-color:var(--teal)}

/* services */
.section-title{left:0;top:315px;width:761px;text-align:center;font-family:"Montserrat",Arial,sans-serif;font-size:9.5px;color:var(--teal);letter-spacing:.4px}
.section-lead{left:240px;top:333px;width:281px;text-align:center;font-size:5px;line-height:9px;color:var(--muted)}
.card-featured{left:310px;top:370px;width:138px;height:181px;background:var(--teal)}
.card{top:370px;width:138px;height:181px;text-align:center}
.card-icon{position:absolute;left:39px;top:15px;width:60px;height:60px;border-radius:50%;border:1px solid #c9c9c9;display:flex;align-items:center;justify-content:center}
.card-title{position:absolute;left:0;top:89px;width:138px;font-family:"Montserrat",Arial,sans-serif;font-size:6.8px;color:#555;letter-spacing:.3px}
.card-rule{position:absolute;left:45px;top:104px;width:48px;height:1px;background:var(--line)}
.card-text{position:absolute;left:12px;top:112px;width:114px;font-size:5px;line-height:9px;color:var(--muted)}
.card-btn{position:absolute;left:44px;top:148px;width:50px;height:16px;border:1px solid #cfcfcf;font-family:"Montserrat",Arial,sans-serif;font-size:4.6px;color:#666;display:flex;align-items:center;justify-content:center;background:var(--white)}
.card.featured .card-icon{border-color:var(--white)}
.card.featured .card-title,.card.featured .card-text{color:var(--white)}
.card.featured .card-rule{background:rgba(255,255,255,.6)}
.card.featured .card-btn{border-color:var(--white);color:var(--teal)}

.divider{left:171px;top:586px;width:419px;height:1px;background:#e6e6e6}

/* profit */
.profit-title{left:171px;top:616px;font-family:"Montserrat",Arial,sans-serif;font-size:9px;color:#444}
.short-rule{width:18px;height:1px;background:#bbb}
.profit-text{left:171px;top:647px;width:152px;font-size:4.9px;line-height:9px;color:var(--muted)}
.small-link{font-family:"Montserrat",Arial,sans-serif;font-size:4.6px;color:#777;letter-spacing:.3px}
.photo{width:119px;height:72px}
.caption{font-family:"Montserrat",Arial,sans-serif;font-size:6.5px;color:#444;letter-spacing:.2px}

/* testimonial */
.testimonial{left:0;top:749px;width:761px;height:167px;background:linear-gradient(180deg,#6a6a6a,#3b3b3b)}
.quote-icon{left:370px;top:779px;width:20px;height:20px;border-radius:50%;border:1.2px solid var(--teal);color:var(--white);font-family:"Montserrat",Arial,sans-serif;font-weight:700;font-size:11px;display:flex;align-items:center;justify-content:center;padding-top:4px}
.quote-text{left:220px;top:813px;width:321px;text-align:center;font-family:"Montserrat",Arial,sans-serif;font-size:7px;line-height:11px;color:var(--white)}
.quote-author{left:0;top:852px;width:761px;text-align:center;font-family:"Montserrat",Arial,sans-serif;font-size:6.8px;color:var(--white);font-style:italic}
.quote-author span{color:var(--teal);font-style:normal;font-weight:600}

/* contact */
.contact{left:0;top:916px;width:761px;height:250px;background:var(--teal)}
.contact-title{top:955px;font-family:"Montserrat",Arial,sans-serif;font-size:9px;color:var(--white);letter-spacing:.2px}
.contact-text{left:171px;top:978px;width:182px;font-size:5px;line-height:9px;color:var(--white)}
.contact-item{left:171px;display:flex;align-items:center;gap:8px;font-family:"Montserrat",Arial,sans-serif;color:var(--white)}
.contact-icon{width:14px;height:14px;border-radius:50%;border:1.2px solid var(--white);display:flex;align-items:center;justify-content:center}
.field{left:399px;width:191px;border:1px solid rgba(255,255,255,.45);font-size:5.8px;color:rgba(255,255,255,.75);padding:5px 9px}
.send-btn{left:399px;top:1116px;width:191px;height:22px;background:var(--white);color:var(--teal);font-family:"Montserrat",Arial,sans-serif;font-size:6.2px;font-weight:500;display:flex;align-items:center;justify-content:center}

/* footer */
.footer-brand{left:172px;top:1179px;font-family:"Montserrat",Arial,sans-serif;font-weight:600;font-size:6px;color:#888}
.footer-copy{left:196px;top:1182px;font-size:4.8px;color:#999}
.social{top:1178px;width:14px;height:14px;border-radius:50%;border:1px solid #999}
</style>
</head>
<body>

<header class="abs site-header">
  <div class="abs brand"><span class="brand-mark"></span>Calloway Holdings</div>
  <span class="abs nav active" style="left:382px">HOME</span>
  <span class="abs nav" style="left:419px">ABOUT US</span>
  <span class="abs nav" style="left:468px">SERVICES</span>
  <span class="abs nav" style="left:514px">CLIENTS</span>
  <span class="abs nav" style="left:554px">CONTACT US</span>
</header>

<section class="abs hero" role="img" aria-label="City street with tall historic buildings and a skyscraper, viewed from below"></section>
<svg class="abs" style="left:101px;top:156px" width="10" height="16" viewBox="0 0 10 16"><path d="M8 1 1 8l7 7" fill="none" stroke="#fff" stroke-width="1.3"/></svg>
<svg class="abs" style="left:650px;top:156px" width="10" height="16" viewBox="0 0 10 16"><path d="M2 1l7 7-7 7" fill="none" stroke="#fff" stroke-width="1.3"/></svg>
<h1 class="abs hero-title">ACHIEVE YOUR <b>GOALS</b> AND LONG-TERM SUCCESS</h1>
<p class="abs hero-sub">PHASELLUS PORTA. FUSCE SUSCT VARIUS MI. CUM SOCIIS NATOQUE PENABUS ET MAGNIS DIS PARTURIENT MONTES, NASCETUR RIDICULUS MUS. NULLA DUI. FUSCE FEUGIAT MALESUADA ODIO.</p>
<div class="abs btn-teal">LEARN MORE</div>
<span class="abs dot" style="left:368px;top:246px"></span>
<span class="abs dot on" style="left:375px;top:246px"></span>
<span class="abs dot" style="left:382px;top:246px"></span>
<span class="abs dot" style="left:389px;top:246px"></span>

<h2 class="abs section-title">WE MEET YOUR FINANCIAL INVESTMENT NEEDS</h2>
<p class="abs section-lead">Sed ut perspiciatis unde omnis iste natus error sit voluptatem accusantium doloremque laudantium,totam rem aperiam, eaque ipsa quae ab illo inventore veritatis et quasi architecto beatae vitae dicta.</p>

<div class="abs card" style="left:166px">
  <div class="card-icon"><svg width="24" height="16" viewBox="0 0 24 16"><rect x="0" y="0" width="24" height="16" rx="2" fill="#c4c4c4"/><rect x="0" y="4" width="24" height="3" fill="#fff"/></svg></div>
  <div class="card-title">PRIVATE BANKING</div>
  <div class="card-rule"></div>
  <p class="card-text">Nemo enim ipsam voluptatem quia voluptas sit aspernatur aut odit aut fugit, sed quia consequuntur</p>
  <div class="card-btn">LEARN MORE</div>
</div>
<div class="abs card featured card-featured">
  <div class="card-icon"><svg width="16" height="22" viewBox="0 0 16 22"><circle cx="8" cy="4" r="3.5" fill="#fff"/><path d="M1 21V12q0-4 4-4h6q4 0 4 4v9z" fill="#fff"/><path d="M8 9l-1.5 2 1.5 7 1.5-7z" fill="#00a990"/></svg></div>
  <div class="card-title">WEALTH MANAGEMENT</div>
  <div class="card-rule"></div>
  <p class="card-text">Nemo enim ipsam voluptatem quia voluptas sit aspernatur aut odit aut fugit, sed quia consequuntur</p>
  <div class="card-btn">LEARN MORE</div>
</div>
<div class="abs card" style="left:452px">
  <div class="card-icon"><svg width="22" height="22" viewBox="0 0 22 22"><circle cx="11" cy="11" r="10" fill="#c4c4c4"/><path d="M11 1v20M1 11h20" stroke="#fff" stroke-width="1"/><text x="11" y="15" text-anchor="middle" font-family="Montserrat,sans-serif" font-weight="700" font-size="11" fill="#fff">$</text></svg></div>
  <div class="card-title">INVESTMENT MANAGEMENT</div>
  <div class="card-rule"></div>
  <p class="card-text">Nemo enim ipsam voluptatem quia voluptas sit aspernatur aut odit aut fugit, sed quia consequuntur</p>
  <div class="card-btn">LEARN MORE</div>
</div>

<div class="abs divider"></div>

<h3 class="abs profit-title">WE WORK FOR YOUR PROFIT!</h3>
<div class="abs short-rule" style="left:172px;top:639px"></div>
<p class="abs profit-text">Lorem ipsum dolor sit amet, consectetur adipiscing elit, sed do eiusmod tempor incididunt ut labore et dolore magna aliqua. Ut enim ad minim veniam, quis nostrud exercitation ullamco laboris nisi</p>
<span class="abs small-link" style="left:172px;top:697px">VIEW ALL</span>

<div class="abs photo" style="left:342px;top:618px;background:linear-gradient(135deg,#6b5a45,#b89a6e 60,#d9c7a3)" role="img" aria-label="Woman working at a desk in a warm-lit office"></div>
<div class="abs caption" style="left:342px;top:700px">INVESTORS</div>
<div class="abs short-rule" style="left:342px;top:712px"></div>
<span class="abs small-link" style="left:342px;top:719px;color:var(--teal)">READ MORE</span>

<div class="abs photo" style="left:471px;top:618px;background:linear-gradient(135deg,#2e3a55,#9aa3b3 55%,#d8d6cf)" role="img" aria-label="Business people reviewing documents and a laptop at a table"></div>
<div class="abs caption" style="left:471px;top:700px">PLANNING &amp; DEVELOPMENT</div>
<div class="abs short-rule" style="left:471px;top:712px"></div>
<span class="abs small-link" style="left:471px;top:719px">READ MORE</span>

<section class="abs testimonial" role="img" aria-label="Black and white photo of business people shaking hands in a meeting"></section>
<div class="abs quote-icon">&ldquo;</div>
<p class="abs quote-text">Lorem ipsum dolor sit amet, consectetur adipisicing elit, sed do eiusmod incididunt ut labore et dolore magna aliqua. Ut enim ad minim veniam...</p>
<p class="abs quote-author"><span>Evan Marsh</span> - USA, Detroit</p>
<span class="abs dot on" style="left:369px;top:883px"></span>
<span class="abs dot" style="left:377px;top:883px"></span>
<span class="abs dot" style="left:385px;top:883px"></span>

<section class="abs contact"></section>
<h3 class="abs contact-title" style="left:171px">CONTACT US</h3>
<p class="abs contact-text">Duis aute irure dolor in reprehenderit in voluptate velit esse cillum dolore eu fugiat nulla pariatur. Excepteur sint occaecat cupidatat non proident, sunt in culpa qui officia deserunt mollit anim id est laborum.</p>
<div class="abs contact-item" style="top:1019px;font-size:6px;line-height:9px">
  <span class="contact-icon"><svg width="6" height="8" viewBox="0 0 6 8"><path d="M3 8C1 5 0 4 0 3a3 3 0 0 1 6 0c0 1-1 2-3 5z" fill="#fff"/><circle cx="3" cy="3" r="1" fill="#00a990"/></svg></span>
  <span>123, Street Name, City Name<br>Country Name 12345</span>
</div>
<div class="abs contact-item" style="top:1050px;font-size:7.5px">
  <span class="contact-icon"><svg width="8" height="6" viewBox="0 0 8 6"><path d="M0 3Q4-1 8 3L7 5 5 4V3Q4 2 3 3v1L1 5z" fill="#fff"/></svg></span>
  <span>(+123) 1234 - 1234</span>
</div>
<div class="abs contact-item" style="top:1082px;font-size:6px">
  <span class="contact-icon"><svg width="7" height="5" viewBox="0 0 7 5"><rect width="7" height="5" fill="#fff"/><path d="M0 0l3.5 3L7 0" fill="none" stroke="#00a990" stroke-width=".8"/></svg></span>
  <span>hello@callowayholdings.com</span>
</div>

<h3 class="abs contact-title" style="left:400px">LEAVE A MESSAGE</h3>
<div class="abs field" style="top:978px;height:20px">Your Name*</div>
<div class="abs field" style="top:1002px;height:20px">Your Email Address*</div>
<div class="abs field" style="top:1028px;height:20px">Phone Number</div>
<div class="abs field" style="top:1054px;height:56px">Message*</div>
<div class="abs send-btn">SEND MESSAGE</div>

<footer>
  <span class="abs footer-brand" style="top:1188px"></span>
  <span class="abs footer-copy" style="left:172px">Calloway Holdings &nbsp;© All Right Reserved 2016. Company Name</span>
  <span class="abs social" style="left:526px" aria-label="Social link"></span>
  <span class="abs social" style="left:543px" aria-label="Social link"></span>
  <span class="abs social" style="left:559px" aria-label="Social link"></span>
  <span class="abs social" style="left:576px" aria-label="Social link"></span>
</footer>

</body>
</html>
```